Business Card Design

I would like a logo created for the top left corner of the card please. I would like a checkerboard in a dark navy with the edges fading out and one random bright orange square.
Updates

I have attached some further notes and a really rough sketch of what I am after.  Thank you. :)

Target Market(s)

Construction, mining, mechanical

Industry/Entity Type

Business

Contact Information for Business Card

KRW Fabrications Pty Ltd, Oscar Plunkett, P. 0413658207, F. 0753917260, E.oscar@krwfabrications.com.au, PO Box 87 WONGARA Q 4571, ABN 52983470611

Font styles to use
Sans Serif

Requirements
Must have
• Really Dark Navy
Really bright Orange

```html
<!DOCTYPE html>
<html lang="en">
<head>
<meta charset="utf-8">
<title>KRW Fabrications – Business Card</title>
<link rel="stylesheet" href="https://fonts.googleapis.com/css2?family=Arimo:wght@400;700&family=Quicksand:wght@500;600&display=swap">
<style>
  :root {
    --navy: #1b1f5e;
    --navy-deep: #13164a;
    --orange: #ffb81c;
    --orange-light: #ffcb4a;
    --white: #ffffff;
    --backdrop: #e9e9ec;
  }
  * { box-sizing: border-box; margin: 0; padding: 0; }
  html, body {
    width: 1200px; height: 885px; overflow: hidden;
    background: var(--backdrop);
  }
  .card {
    position: absolute; left: 150px; top: 185px;
    width: 900px; height: 514px;
    background: var(--white);
    box-shadow: 0 8px 24px rgba(0,0,0,0.18);
    overflow: hidden;
  }
  .card__band {
    position: absolute; left: 0; right: 0; top: 283px; bottom: 0;
    background: linear-gradient(115deg, #2a2f72 0%, var(--navy) 45%, var(--navy-deep) 100%);
    border-top: 5px solid var(--orange);
  }
  .brand {
    position: absolute; left: 60px; top: 92px;
    display: flex; align-items: center; gap: 18px;
  }
  .brand__square {
    width: 34px; height: 34px; background: var(--orange);
  }
  .brand__name {
    font-family: "Arimo", Arial, sans-serif;
    font-weight: 700; font-size: 46px; letter-spacing: -0.5px;
    color: var(--navy);
  }
  .name-tag {
    position: absolute; left: 560px; top: 245px;
    width: 310px; height: 70px;
    background: linear-gradient(180deg, var(--orange-light), var(--orange));
    border: 4px solid var(--white);
    border-radius: 26px;
    display: flex; align-items: center; justify-content: center;
    font-family: "Arimo", Arial, sans-serif;
    font-size: 34px; color: var(--navy);
  }
  .postal {
    position: absolute; left: 60px; top: 330px;
    font-family: "Quicksand", sans-serif; font-weight: 600;
    font-size: 20px; line-height: 1.35; letter-spacing: 1px;
    color: var(--orange);
  }
  .contacts {
    position: absolute; left: 520px; top: 345px;
    list-style: none;
    font-family: "Quicksand", sans-serif; font-weight: 600;
    font-size: 21px; line-height: 1.6; letter-spacing: 1px;
    color: var(--white);
  }
  .contacts__label { color: var(--orange); margin-right: 10px; }
</style>
</head>
<body>
  <article class="card">
    <div class="brand">
      <span class="brand__square"></span>
      <span class="brand__name">KRW Fabrications Pty Ltd</span>
    </div>
    <div class="card__band"></div>
    <div class="name-tag">Oscar Plunkett</div>
    <p class="postal">PO Box 87 WONGARA Q 4571<br>ABN 52 983 470 611</p>
    <ul class="contacts">
      <li><span class="contacts__label">P.</span>0413 658 207</li>
      <li><span class="contacts__label">F.</span>07 5391 7260</li>
      <li><span class="contacts__label">E.</span>oscar@krwfabrications.com.au</li>
    </ul>
  </article>
</body>
</html>
```